Vantage 9 Builders, Inc Biz Cards

Vantage 9 Builders, Inc is a turnkey building solution provider in the Greater Philadelphia Area. We work collaboratively with clients to provide turnkey building services in both the residential and commercial markets.
We are targeting the higher end clients in the commercial market. We have been successful in getting a few commercial projects in , but still rely on our residential work for a large portion of our revenue. We are trying to move almost exclusively toward the commercial market.
Services include;
-Commercial New Construction and Interior Tenant Fit-Outs
-Residential New Construction and Renovations
-Project Management and Owner's Representative Services
Target Market(s)
Tenants in large commerical buildings, higher end home owners, someone with a known budget and dream but unsure how to make it a building reality
Industry/Entity Type
Residential
Contact Information for Business Card
Vantage 9 Builders, Inc.
415 Maple Hollow
Jeffersonville, PA 19876
There are three people that we need to order business cards for.
Dale Hunt
Cell# 484-555-0193
Dale@Vantage-9-Builders.example
Rory Velluzzi
Cell# 610-555-0147
Rory@Vantage-9-Builders.example
Ned Fox
Cell# 267-555-0128
Ned@Vantage-9-Builders.example
HIC#PA574920
www.vantage-9-builders.example (under construction)
We like our written our logo Vantage 9 Builders, Inc with red, blue, and grey. We do not like the V9B with spinning arrows as, however like the incorporation of the spinning around arrows to represent "turnkey" building services.
Look and feel

```html
<!DOCTYPE html>
<html lang="en">
<head>
<meta charset="utf-8">
<title>Vantage 9 Builders – Business Card</title>
<link rel="stylesheet" href="https://fonts.googleapis.com/css2?family=Montserrat:wght@400;500;700&display=swap">
<style>
  :root {
    --red-core: #e61e27;
    --red-edge: #861d1b;
    --blue-dark: #0b3f8e;
    --blue-light: #0a8ed6;
    --brand-blue: #1b6fc2;
    --accent-red: #b51f24;
    --heading-blue: #1160a8;
    --text-grey: #6b6b6b;
    --white: #ffffff;
  }
  * { margin: 0; padding: 0; box-sizing: border-box; }
  html, body {
    width: 1200px;
    height: 741px;
    overflow: hidden;
    background: var(--white);
    font-family: "Montserrat", sans-serif;
  }
  .card {
    position: relative;
    width: 1200px;
    height: 741px;
    background: var(--white);
  }
  .hero {
    position: absolute;
    left: 0; top: 0;
    width: 1200px;
    height: 492px;
    background:
      linear-gradient(90deg, var(--red-edge) 0%, #b01d22 22%, var(--red-core) 50%, #b01d22 78%, var(--red-edge) 100%);
    display: flex;
    flex-direction: column;
    align-items: center;
  }
  .brand-name {
    margin-top: 232px;
    font-weight: 700;
    font-size: 74px;
    line-height: 1;
    letter-spacing: 1px;
    text-transform: uppercase;
    color: var(--brand-blue);
    white-space: nowrap;
  }
  .tagline {
    margin-top: 20px;
    font-weight: 400;
    font-size: 32px;
    line-height: 1;
    color: var(--white);
  }
  .stripe-blue {
    position: absolute;
    left: 0; top: 492px;
    width: 1200px;
    height: 25px;
    background: linear-gradient(90deg, var(--blue-dark) 0%, #0f5aa8 45%, var(--blue-light) 100%);
  }
  .stripe-red {
    position: absolute;
    left: 0; top: 517px;
    width: 1200px;
    height: 4px;
    background: var(--accent-red);
  }
  .services {
    position: absolute;
    left: 0; top: 543px;
    width: 1200px;
    text-align: center;
  }
  .services-heading {
    font-weight: 400;
    font-size: 24px;
    line-height: 30px;
    color: var(--heading-blue);
    text-transform: uppercase;
  }
  .services-list {
    list-style: none;
    font-weight: 400;
    font-size: 26px;
    line-height: 29px;
    color: var(--text-grey);
  }
</style>
</head>
<body>
  <main class="card">
    <section class="hero">
      <h1 class="brand-name">Vantage 9 Builders</h1>
      <p class="tagline">A Full Service Construction Company</p>
    </section>
    <div class="stripe-blue"></div>
    <div class="stripe-red"></div>
    <section class="services">
      <h2 class="services-heading">Services:</h2>
      <ul class="services-list">
        <li>Commercial Construction and Interior Fit-Outs</li>
        <li>Residential Construction and Renovations</li>
        <li>Project Management and Owner’s Representative Services</li>
      </ul>
    </section>
  </main>
</body>
</html>
```